New Corporate website more focused on funnel and great design

Our company, Bold Harbor needs a new website to look like it's from 2021. We work with large businesses in the corporte world and need to reflect that we are professional, focused on our clients, and trsutworthy. It should include some/most of the components from our current site: boldharbor.com but should focus more about getting people to optin to out free downloads, which can be found on this page: https://www.boldharbor.com/get-started-with-a-prep-session/ and this page: https://www.boldharbor.com/team-onboarding/

Our new website should do a better job at explaining what we do, who we serve, and how we fix their problems of onboarding new leaders. Feel free to use dummy text if you are not sure what to put in for certain sections. I also would like to point out that most of the audiance is older, so we don't need anything too younge and flashy, or that is hard it use. it should have big clear fonts, plently of contrast, and work well for poeple who are not good at using the internet. Please use the colors of the logo, and you can add another color or two if you think it's fits

Industry/Entity Type

business consulting

Number of Pages Required

2 page

Font styles to use
Sans Serif

Requirements
Must have
• corporate feel, look professional, focus on getting new leads
Should not have
• cute or children feel

```html
<!DOCTYPE html>
<html lang="en">
<head>
<meta charset="utf-8">
<title>Bold Harbor — Better Results Faster</title>
<link href="https://fonts.googleapis.com/css2?family=Jost:wght@300;400;500;600&family=Nunito+Sans:ital,wght@0,400;0,600;0,700;1,400&display=swap" rel="stylesheet">
<style>
:root{
  --navy:#1f4e86;
  --navy-dark:#173d6b;
  --green:#8ab43f;
  --ink:#1d2634;
  --body:#555b66;
  --mist:#eef1f6;
  --line:#c9d0da;
  --footer:#2b2b2b;
  --white:#ffffff;
}
*{box-sizing:border-box;margin:0;padding:0}
html,body{width:1200px;height:3947px;overflow:hidden}
body{font-family:"Nunito Sans",sans-serif;color:var(--ink);background:var(--white);position:relative}
.abs{position:absolute}
.heading{font-family:"Jost",sans-serif;font-weight:400;text-transform:uppercase;letter-spacing:.5px}
.btn{position:absolute;display:flex;align-items:center;justify-content:center;border-radius:20px;color:var(--white);font-family:"Jost",sans-serif;font-weight:500;font-size:11px;letter-spacing:1px;text-transform:uppercase}
.btn--navy{background:var(--navy)}
.btn--green{background:var(--green)}
.wordmark{font-family:"Jost",sans-serif;font-weight:500;color:var(--navy);display:flex;align-items:center;gap:10px}
.wordmark .mark{width:30px;height:30px;background:var(--navy)}

/* header */
.site-header{position:absolute;left:0;top:0;width:1200px;height:95px}
.site-header .wordmark{left:87px;top:28px;font-size:30px}
.contact-line{left:644px;top:22px;font-size:14px;color:var(--green);font-weight:600}
.contact-line span{color:var(--navy)}
.social{display:flex;gap:8px}
.social i{display:block;width:25px;height:25px;border-radius:50%;border:1.5px solid var(--navy)}
.social i.filled{background:var(--navy)}
.site-header .social{position:absolute;left:1022px;top:19px}
.main-nav{position:absolute;top:62px;left:486px;display:flex;gap:36px;font-family:"Jost",sans-serif;font-size:11.5px;font-weight:500;letter-spacing:.5px;color:var(--ink)}
.main-nav .active{color:var(--navy)}

/* hero */
.hero{position:absolute;left:0;top:95px;width:1200px;height:521px;background:linear-gradient(100deg,#3e4348 0%,#6d7378 45%,#a9acae 100%)}
.hero h1{position:absolute;left:87px;top:135px;font-size:38px;line-height:46px;color:var(--white);font-weight:400}
.hero .btn{left:87px;top:349px;width:128px;height:30px}
.dots{position:absolute;left:87px;top:470px;display:flex;gap:9px}
.dots i{width:12px;height:12px;border-radius:50%;border:1.5px solid var(--white)}

/* intro */
.intro-rule{left:207px;top:699px;width:3px;height:182px;background:var(--navy)}
.intro-title{left:243px;top:692px;font-size:27px;line-height:35px;color:var(--ink)}
.plan-first{font-family:"Jost",sans-serif;color:var(--navy);text-transform:uppercase}
.intro-plan{left:243px;top:798px}
.plan-first .small{font-size:19px}
.plan-first .big{font-size:46px;font-weight:500}
.plan-first .sub{display:block;font-size:19px;letter-spacing:.5px;margin-top:-4px}
.intro-copy{left:680px;top:694px;width:330px;font-size:12px;line-height:22.5px;color:var(--body)}
.intro-copy p+p{margin-top:21px}
.intro-about{left:680px;top:972px;width:120px;height:32px}

/* tabs */
.tab{position:absolute;left:0;width:420px;height:120px;background:var(--mist)}
.tab .num{position:absolute;left:87px;top:-15px;width:30px;height:30px;border-radius:50%;background:var(--white);border:1.5px solid var(--line);font-size:12px;display:flex;align-items:center;justify-content:center;color:var(--navy);font-weight:700}
.tab .label{position:absolute;left:87px;top:46px;font-size:19px;color:var(--navy);font-weight:600}
.tab--active{background:var(--navy)}
.tab--active .label{color:var(--white)}
.tab-arrow{position:absolute;left:420px;top:1205px}
.merge-panel{position:absolute;left:420px;top:1144px;width:780px;height:360px;background:linear-gradient(120deg,#3b4047,#5c6168 55%,#3f444a)}
.merge-panel .copy{position:absolute;left:0;width:780px;text-align:center;color:var(--white)}
.merge-panel h2{top:54px;font-size:28px;line-height:34px;font-weight:400}
.merge-panel .lead{top:138px;font-size:18px}
.merge-panel .detail{top:179px;font-size:13.5px;line-height:20px}
.merge-panel .btn{left:330px;top:265px;width:120px;height:30px}

/* industries */
.section-title{font-size:27px;color:var(--ink)}
.industry-title{left:0;top:1578px;width:1200px;text-align:center}
.industry{position:absolute;top:1645px;width:240px;text-align:center}
.industry .ring{width:160px;height:160px;margin:0 auto;border-radius:50%;border:1.5px solid var(--navy);display:flex;align-items:center;justify-content:center}
.industry .name{margin-top:18px;font-family:"Jost",sans-serif;font-weight:500;font-size:13px;line-height:17px;text-transform:uppercase;color:var(--ink)}
.chev{position:absolute;top:1708px}
.industry-btn{left:512px;top:1891px;width:176px;height:30px}

/* articles */
.articles{position:absolute;left:0;top:2002px;width:1200px;height:515px;background:var(--mist)}
.articles .section-title{left:87px;top:73px}
.articles .btn{left:967px;top:76px;width:145px;height:30px}
.card{position:absolute;top:142px;width:321px}
.card .photo{width:321px;height:200px}
.card .cat{margin-top:30px;font-size:10px;letter-spacing:.5px;color:var(--navy);font-weight:600;text-transform:uppercase}
.card .title{margin-top:6px;font-size:18px;line-height:23px;color:var(--ink);font-weight:600}
.card .title.linked{color:var(--navy);text-decoration:underline}

/* download */
.dl-rule{left:87px;top:2574px;width:3px;height:246px;background:var(--navy)}
.dl-brand{left:125px;top:2612px;font-size:40px}
.dl-brand .mark{width:44px;height:44px}
.dl-plan{left:127px;top:2722px}
.field{position:absolute;left:464px;width:384px;height:32px;border:1.5px solid var(--line);border-radius:18px;font-size:11px;color:var(--body);padding:8px 18px}
.dl-btn{left:464px;top:2764px;width:152px;height:32px}
.stat{position:absolute;left:950px;top:2597px;width:164px;text-align:center}
.stat .num{position:absolute;left:0;top:52px;width:164px;font-family:"Jost",sans-serif;font-size:50px;font-weight:500;color:var(--ink)}
.stat .cap{margin-top:10px;font-family:"Jost",sans-serif;font-weight:500;font-size:13px;line-height:17px;color:var(--ink);text-transform:uppercase}

/* testimonials */
.testimonials{position:absolute;left:0;top:2876px;width:1200px;height:608px;background:var(--navy);color:var(--white)}
.testimonials .section-title{left:0;top:80px;width:1200px;text-align:center;color:var(--white)}
.client{position:absolute;top:142px;width:184px;height:95px;background:var(--white);display:flex;align-items:center;justify-content:center;gap:8px;font-size:26px;font-weight:600;color:var(--navy)}
.client .dot{width:18px;height:18px;background:var(--navy)}
.client-notch{position:absolute;left:690px;top:237px;width:0;height:0;border-left:12px solid transparent;border-right:12px solid transparent;border-top:12px solid var(--white)}
.quote-mark{left:0;top:268px;width:1200px;text-align:center;font-family:"Jost",sans-serif;font-size:64px;line-height:64px}
.quote{left:0;top:326px;width:1200px;text-align:center;font-style:italic;font-size:14px;line-height:22.5px}
.author{left:0;top:418px;width:1200px;text-align:center;font-family:"Jost",sans-serif;font-weight:500;font-size:13px;letter-spacing:.5px}
.role{left:0;top:440px;width:1200px;text-align:center;font-size:11.5px}
.testimonials .btn{left:524px;top:491px;width:152px;height:30px}

/* footer */
.site-footer{position:absolute;left:0;top:3484px;width:1200px;height:463px;background:var(--footer);color:#cfd2d6}
.site-footer .wordmark{left:87px;top:76px;font-size:26px;color:var(--white)}
.site-footer .wordmark .mark{background:var(--white);width:26px;height:26px}
.f-phones{left:87px;top:148px;font-size:18px;line-height:27px;color:#e2e4e7}
.f-tag{left:87px;top:232px;font-size:13px;color:var(--navy);letter-spacing:.3px}
.site-footer .social{position:absolute;left:87px;top:290px;gap:12px}
.site-footer .social i{border:none;background:var(--navy)}
.site-footer .social i.alt{background:var(--green)}
.f-head{font-family:"Jost",sans-serif;font-weight:500;font-size:13px;color:var(--white);text-transform:uppercase}
.f-links{left:420px;top:126px;font-size:11.5px;line-height:29px;color:#bfc3c8;list-style:none}
.f-field{position:absolute;top:148px;width:158px;height:32px;background:var(--white);border-radius:18px;font-size:11px;color:#444;padding:8px 16px}
.f-message{position:absolute;left:615px;top:206px;width:497px;height:96px;background:var(--white);border-radius:12px;font-size:11px;color:#444;padding:12px 16px}
.site-footer .btn{left:615px;top:324px;width:209px;height:30px}
.f-legal{top:392px;font-size:11px;color:#bfc3c8}
.f-legal b{color:var(--white);font-weight:600}
</style>
</head>
<body>

<header class="site-header">
  <div class="abs wordmark"><span class="mark"></span>Bold Harbor</div>
  <div class="abs contact-line">☏ US: <span>+1 555.010.4821</span> &nbsp;|&nbsp; UK: <span>+44 (0) 7700 900123</span></div>
  <div class="social"><i class="filled"></i><i></i><i></i></div>
  <nav class="main-nav"><span class="active">HOME</span><span>WHO WE ARE</span><span>WHAT WE DO</span><span>CLIENTS</span><span>BLOG</span><span>RESOURCES</span><span>CONTACT</span></nav>
</header>

<section class="hero" role="img" aria-label="Photo of business leaders in a meeting around a conference table">
  <h1 class="heading">Accelerate business<br>performance during<br>critical leadership<br>transitions</h1>
  <div class="btn btn--navy">Contact us</div>
  <div class="dots"><i></i><i></i><i></i></div>
</section>

<div class="abs intro-rule"></div>
<h2 class="abs heading intro-title">Transitions are a<br>crucible of leadership</h2>
<div class="abs plan-first intro-plan"><span class="small">First </span><span class="big">100 Day</span><span class="sub">Action plan process</span></div>
<div class="abs intro-copy">
  <p>We know, through our personal experiences gained as leaders, that the first 100 days in a critical transition are a crucible of leadership – when managed well, leaders build cohesive teams that succeed. When managed poorly, leaders falter, teams stall, and organizations fail.</p>
  <p>These experiences, and our motivation to make things better for leaders during critical transitions, became the initial catalyst for the creation of the tools that became the core ...</p>
</div>
<div class="btn btn--green intro-about">About us</div>

<div class="tab" style="top:1085px"><span class="num">1</span><span class="label">Executive Onboarding</span></div>
<div class="tab tab--active" style="top:1205px"><span class="num">2</span><span class="label">Team Onboarding</span></div>
<div class="tab" style="top:1325px"><span class="num">3</span><span class="label">Acceleration &amp; Restart</span></div>
<div class="merge-panel" role="img" aria-label="Photo of an executive team meeting in a bright office">
  <h2 class="copy heading">About to combine two or<br>more teams?</h2>
  <p class="copy lead">Now, you'll need to deliver on the promise of the investment.</p>
  <p class="copy detail">80% of mergers &amp; acquisitions fail to boost returns.<br>Why? Inability to realize synergies and optimize the combined team to<br>enhance competitiveness.</p>
  <div class="btn btn--navy">Learn more</div>
</div>
<svg class="tab-arrow" width="60" height="120" viewBox="0 0 60 120"><polygon points="0,0 60,60 0,120" fill="#1f4e86"/></svg>

<h2 class="abs heading section-title industry-title">Industry we serve</h2>
<svg class="chev" style="left:193px" width="20" height="40" viewBox="0 0 20 40"><polyline points="17,3 3,20 17,37" fill="none" stroke="#8a93a0" stroke-width="2"/></svg>
<svg class="chev" style="left:985px" width="20" height="40" viewBox="0 0 20 40"><polyline points="3,3 17,20 3,37" fill="none" stroke="#8a93a0" stroke-width="2"/></svg>
<div class="industry" style="left:243px">
  <div class="ring"><svg width="64" height="60" viewBox="0 0 64 60"><polygon points="32,2 62,16 2,16" fill="#1f4e86"/><rect x="4" y="18" width="56" height="4" fill="#1f4e86"/><g fill="#1f4e86"><rect x="8" y="25" width="6" height="24"/><rect x="19" y="25" width="6" height="24"/><rect x="30" y="25" width="6" height="24"/><rect x="41" y="25" width="6" height="24"/><rect x="52" y="25" width="6" height="24"/></g><rect x="2" y="52" width="60" height="6" fill="#1f4e86"/></svg></div>
  <div class="name">Banking</div>
</div>
<div class="industry" style="left:477px">
  <div class="ring"><svg width="68" height="56" viewBox="0 0 68 56"><rect x="3" y="3" width="26" height="50" rx="13" fill="none" stroke="#1f4e86" stroke-width="4"/><line x1="3" y1="28" x2="29" y2="28" stroke="#1f4e86" stroke-width="4"/><rect x="30" y="12" width="24" height="40" rx="12" transform="rotate(-40 42 32)" fill="none" stroke="#1f4e86" stroke-width="4"/><line x1="30" y1="40" x2="54" y2="24" stroke="#1f4e86" stroke-width="4"/></svg></div>
  <div class="name">Pharmaceutical, and<br>life sciences</div>
</div>
<div class="industry" style="left:716px">
  <div class="ring"><svg width="50" height="60" viewBox="0 0 50 60"><path d="M25 3 C30 16 46 24 46 39 C46 51 36 57 25 57 C14 57 4 51 4 39 C4 29 12 22 15 14 C18 22 20 25 23 27 C26 19 26 11 25 3 Z" fill="none" stroke="#1f4e86" stroke-width="4" stroke-linejoin="round"/><path d="M25 34 C28 40 33 43 33 48 C33 52 29 55 25 55 C21 55 17 52 17 48 C17 43 22 40 25 34 Z" fill="none" stroke="#1f4e86" stroke-width="3.5"/></svg></div>
  <div class="name">Energy</div>
</div>
<div class="btn btn--green industry-btn">View all industry</div>

<section class="articles">
  <h2 class="abs heading section-title">Recent articles</h2>
  <div class="btn btn--navy">View all news</div>
  <article class="card" style="left:87px">
    <div class="photo" role="img" aria-label="Photo of an office worker carrying a box and party balloons" style="background:linear-gradient(135deg,#5a5148,#a99a86 60%,#7b7064)"></div>
    <div class="cat">Ongoing comunication</div>
    <div class="title">When to use the three different ways to fire employees</div>
  </article>
  <article class="card" style="left:439px">
    <div class="photo" role="img" aria-label="Photo of executives testifying at a hearing table" style="background:linear-gradient(135deg,#3d3430,#8c7f74 55%,#4a4440)"></div>
    <div class="cat">First time leaders</div>
    <div class="title linked">Why Vextor's new CFO should fail, but won't</div>
  </article>
  <article class="card" style="left:790px">
    <div class="photo" role="img" aria-label="Photo of a football coach shouting on the sideline" style="background:linear-gradient(135deg,#2f4a3a,#6e7f73 55%,#3b4a5a)"></div>
    <div class="cat">Executive onboarding, messaging</div>
    <div class="title">How to elevate involved participants to committed champions</div>
  </article>
</section>

<div class="abs dl-rule"></div>
<div class="abs wordmark dl-brand"><span class="mark"></span>Bold Harbor</div>
<div class="abs plan-first dl-plan"><span class="small">First </span><span class="big">100 Day</span><span class="sub">Action plan process</span></div>
<div class="field" style="top:2598px">First Name*</div>
<div class="field" style="top:2653px">Last Name*</div>
<div class="field" style="top:2707px">Email Address*</div>
<div class="btn btn--green dl-btn">Download now!</div>
<div class="stat">
  <svg width="164" height="164" viewBox="0 0 164 164"><circle cx="82" cy="82" r="79" fill="none" stroke="#dfe3e8" stroke-width="3"/><circle cx="82" cy="82" r="79" fill="none" stroke="#1f4e86" stroke-width="3" stroke-dasharray="446.7 496.4" transform="rotate(-90 82 82)"/></svg>
  <div class="num">90%</div>
  <div class="cap">90% of our<br>clients succeed</div>
</div>

<section class="testimonials">
  <h2 class="abs heading section-title">What our clients are saying</h2>
  <svg class="abs" style="left:140px;top:177px" width="14" height="26" viewBox="0 0 14 26"><polyline points="12,2 2,13 12,24" fill="none" stroke="#fff" stroke-width="2"/></svg>
  <svg class="abs" style="left:1046px;top:177px" width="14" height="26" viewBox="0 0 14 26"><polyline points="2,2 12,13 2,24" fill="none" stroke="#fff" stroke-width="2"/></svg>
  <div class="client" style="left:208px">Corvane</div>
  <div class="client" style="left:408px">Northell</div>
  <div class="client" style="left:608px"><span class="dot"></span>Boxwell</div>
  <div class="client" style="left:808px">TrueCrest</div>
  <div class="client-notch"></div>
  <div class="abs quote-mark">66</div>
  <p class="abs quote">" The Bold Harbor process helped me get an early start on learning, relationships and my messaging.<br>It has helped me develop credibility and trusting relationships in a founder-led company<br>with a very strong culture. This is priceless "</p>
  <div class="abs author">MARION ELLSWORTH</div>
  <div class="abs role">CMO, Boxwell</div>
  <div class="btn btn--green">View all clients</div>
</section>

<footer class="site-footer">
  <div class="abs wordmark"><span class="mark"></span>Bold Harbor</div>
  <div class="abs f-phones">US: +1 555.010.4821<br>UK: +44 (0) 7700 900123</div>
  <div class="abs f-tag">BETTER RESULTS FASTER Since 2003</div>
  <div class="social"><i></i><i class="alt"></i><i></i></div>
  <div class="abs f-head" style="left:420px;top:80px">Quick links</div>
  <ul class="abs f-links"><li>Home</li><li>Who We Are</li><li>What We Do</li><li>Clients</li><li>Blog</li><li>Resources</li><li>Contact</li></ul>
  <div class="abs f-head" style="left:615px;top:80px">Speak to one of our partners today</div>
  <div class="f-field" style="left:615px">Name</div>
  <div class="f-field" style="left:784px">Phone</div>
  <div class="f-field" style="left:954px">Email</div>
  <div class="f-message">Message ...</div>
  <div class="btn btn--navy">Speak to a partner today</div>
  <div class="abs f-legal" style="left:87px">© 2021 <b>Bold Harbor.</b> All Rights Reserved</div>
  <div class="abs f-legal" style="left:615px">Privacy Policy &nbsp;&nbsp;&nbsp;|&nbsp;&nbsp;&nbsp; Terms &amp; Conditions</div>
</footer>

</body>
</html>
```